Unique Realty Niche needs a web design

Starting Note: Please do not use the colors from the logo on keyplotmeadowdoors.example which is their current website. This logo will eventually change but it is what they have now.

This website is a realty website that caters to individuals who want to rent out their homes (investors) and those who want to rent a home (Tenants). We provide no credit check to rent a home from a investor at a higher cost for the tenant to balance risk. Good renters with bad credit are able to rent or buy a house from investors who are registered in our system.

Target Market(s)

Home Owners trying to rent out their homes, and people looking to rent.

Industry/Entity Type

House

Requirements
Must have
• Main Navigation links: Home - Our Story - tenant - owner - contact us

A log in form somewhere on the page.

Key themes in the site are as follows: The site needs to be clean and professional looking i.e. no grunge. I provided some color palettes below, these are not set in stone and if you know of a good palette(s) our client is very open to all suggestions. The main navigation needs to stay on top but other on page navigations could go on left (preferably) On the left or the right will be featured listings for some homes. It will be between 3 to 5 listings showing at one time. (Please see keyplotmeadowdoors.example for example)

Example Color Palettes:
http://hueboard.example/#themeID/1000001
http://hueboard.example/#themeID/100002
http://hueboard.example/#themeID/1000003
http://hueboard.example/#themeID/1000004

Example Websites That Client Likes:
NOTE: Very Flexible, no need to duplicate these below.
http://www.lanternestatesgrove.example/
http://www.vkhquarry.example/
http://www.tufelbrookstewards.example/index.php?pr=Home_Page

Nice to have
• It would be nice to have short easy to read paragraphs accompanied by a photo so scanning is easy on the site. Then in later pages we will have more text when there is more detail needed. We know you wont come up with the content but concept would be nice.

```html
<!DOCTYPE html>
<html lang="en">
<head>
<meta charset="utf-8">
<title>Keyplot Meadow Doors</title>
<link rel="stylesheet" href="https://fonts.googleapis.com/css2?family=Arimo:wght@400;700&family=Oswald:wght@400;600&family=Tinos&display=swap">
<style>
:root{
  --header-blue:#4682ae;
  --hero-top:#3d79a6;
  --hero-bottom:#3b8fc3;
  --nav-gray:#dcdfe2;
  --nav-text:#2f4a5e;
  --tab-dark:#2f6c98;
  --panel:#5596c4;
  --panel-dark:#3b78a5;
  --tab-light:#bfe6ee;
  --featured:#3a6f98;
  --card-cap:#6f9ec2;
  --red:#c8080c;
  --red-deep:#9e0306;
  --gold:#ffd23a;
  --snow:#eef3f8;
  --list-blue:#3f78aa;
  --band:#5a8db5;
  --footer:#4a7ba3;
  --footer-text:#dbe8f2;
  --orange:#f47d1e;
  --white:#fff;
}
*{box-sizing:border-box;margin:0;padding:0}
html,body{width:853px;height:1200px;overflow:hidden}
body{position:relative;background:var(--white);font-family:"Arimo",Arial,sans-serif;color:var(--white)}
.abs{position:absolute}

/* header */
.site-header{left:0;top:0;width:853px;height:75px;background:linear-gradient(var(--header-blue),#3f7aa6)}
.brand{left:106px;top:12px;display:flex;align-items:center;gap:6px}
.brand-mark{width:16px;height:16px;background:var(--white)}
.brand-name{font-family:"Tinos",serif;font-size:20px;color:var(--white)}
.tagline{left:128px;top:49px;font-size:10px;font-weight:700}
.phone{left:591px;top:45px;font-family:"Tinos",serif;font-size:17px}

/* nav */
.main-nav{left:0;top:75px;width:853px;height:28px;background:var(--nav-gray);border-bottom:1px solid #c7ccd0}
.main-nav a{position:absolute;top:8px;font-size:11px;color:var(--nav-text);text-decoration:none}
.main-nav a.active{top:4px;height:24px;padding:5px 10px 0;background:var(--tab-dark);color:var(--white);border-radius:7px 7px 0 0}
.account{left:644px}

/* hero */
.hero{left:0;top:103px;width:853px;height:265px;background:linear-gradient(var(--hero-top),var(--hero-bottom))}
.slider{left:111px;top:119px;width:339px;height:226px;background:#e8dfdc;padding:6px}
.slide-photo{width:100%;height:100%;background:linear-gradient(#8fa9c4 0%,#c3ccd2 35%,#5b5a3c 60%,#2d3323 100%);position:relative}
.slide-caption{position:absolute;left:0;bottom:0;width:100%;height:44px;background:rgba(0,0,0,.55);padding:6px 17px}
.slide-caption h3{font-size:13px;font-weight:400}
.slide-caption p{font-size:9px;margin-top:3px}
.dots{left:238px;top:353px;display:flex;gap:4px}
.dots i{width:7px;height:7px;border-radius:50%;background:var(--white)}
.dots i.off{background:#8fb3cf}

.search-tab{top:119px;height:29px;border-radius:6px 6px 0 0;font-size:15px;font-weight:700;padding:7px 0 0;text-align:center}
.tab-tenants{left:470px;width:103px;background:var(--panel-dark)}
.tab-owners{left:578px;width:88px;background:var(--tab-light);color:#3b88b0}
.search-panel{left:470px;top:147px;width:278px;height:210px;background:rgba(110,165,205,.55);border-radius:0 8px 8px 8px}
.search-panel label,.search-panel .lbl{position:absolute;font-size:10.5px}
.field{position:absolute;left:21px;top:38px;width:227px;height:30px;background:var(--white);border:2px solid #9dc3dc;border-radius:4px;color:#4a6e8a;font-size:11px;padding:6px 11px}
.check{position:absolute;left:29px;top:77px;width:11px;height:11px;background:var(--white);border-radius:2px}
.select{position:absolute;left:113px;width:134px;height:21px;background:var(--white);border-radius:3px;color:#55708a;font-size:9.5px;padding:4px 14px}
.select svg{position:absolute;right:5px;top:5px}
.btn-search{position:absolute;left:110px;top:177px;width:139px;height:29px;border:2px solid #d8e9f4;border-radius:5px;background:linear-gradient(#6fb1e0,#3f8dc6);font-size:14px;text-align:center;padding-top:5px}

/* promo */
.promo{left:111px;top:380px;width:437px;height:506px;border:1px solid #e3e8ec;background:var(--white)}
.promo-red{position:absolute;left:0;top:0;width:437px;height:150px}
.badge{position:absolute;left:10px;top:17px;width:104px;height:104px;border-radius:50%;background:radial-gradient(circle at 40% 35%,#e20c12,var(--red-deep));color:var(--gold);font-family:"Oswald",sans-serif;text-align:center}
.badge b{display:block;font-size:30px;font-weight:600;transform:rotate(-18deg);margin-top:16px}
.badge span{display:block;font-size:18px;transform:rotate(-18deg);margin-top:-8px;margin-left:22px}
.holiday{position:absolute;left:140px;top:14px;width:290px;text-align:center;font-family:"Oswald",sans-serif}
.holiday h2{font-size:21px;font-weight:600;letter-spacing:.5px}
.holiday .sub{font-size:10px;color:var(--gold);margin-top:-2px}
.holiday .ask{font-size:13.5px;color:var(--gold);margin-top:10px;line-height:1.4}
.perks{position:absolute;left:18px;top:149px;font-family:"Oswald",sans-serif;font-size:10px;line-height:18px;color:#3a6a94;font-weight:600}
.listings{position:absolute;left:21px;top:228px;list-style:none;font-size:10.2px;line-height:20px;color:var(--list-blue)}

/* featured */
.featured{left:561px;top:379px;width:191px;height:507px;background:var(--featured);border-radius:2px}
.featured h2{position:absolute;left:16px;top:7px;font-size:13px;font-weight:400}
.card{position:absolute;left:14px;width:161px;height:145px;background:var(--card-cap);border:3px solid #dfe6ec;border-bottom:none}
.card-photo{height:103px;background:linear-gradient(#5f9bd6 0%,#9ec3e6 35%,#7d4b3b 55%,#4e7a3a 80%,#3c6a2c 100%)}
.card p{position:absolute;left:6px;top:108px;font-size:11px;line-height:14px}
.card svg{position:absolute;right:8px;top:112px}

/* bottom band */
.band{left:0;top:915px;width:853px;height:132px;background:var(--band)}
.box{top:924px;height:73px;border:1px solid #cfe0ec;border-radius:4px;background:rgba(255,255,255,.12)}
.box h3{position:absolute;left:16px;top:7px;font-size:14.5px;font-weight:400}
.input{position:absolute;top:36px;height:21px;background:var(--white);border-radius:2px;color:#6a8aa3;font-size:11px;padding:3px 9px}
.btn-small{position:absolute;top:35px;height:23px;border:2px solid #d6e7f2;border-radius:5px;background:linear-gradient(#6cb0dc,#3e8cc3);font-size:11px;text-align:center;padding-top:3px}
.signup{left:108px;top:1005px;width:314px;height:31px;border-radius:3px;overflow:hidden;border:1px solid #d6e7f2}
.signup .left{position:absolute;left:0;top:0;width:207px;height:100%;background:#74a8cf;font-size:14.5px;padding:6px 0 0 31px}
.signup .right{position:absolute;left:201px;top:0;width:113px;height:100%;background:var(--orange);clip-path:polygon(6px 0,100% 0,100% 100%,6px 100%,0 50%);font-size:14.5px;padding:6px 0 0 22px}
.social{top:1005px;width:30px;height:30px;border-radius:4px;background:#2f5f86;border:1px solid #9fc2db}

/* footer */
.site-footer{left:0;top:1047px;width:853px;height:153px;background:var(--footer)}
.col{position:absolute;top:15px;font-size:8.6px;color:var(--footer-text);line-height:14.7px}
.col h4{font-size:10.5px;color:var(--white);margin-bottom:6px}
.col ul{list-style:none}
.col .sign{font-weight:700;color:var(--white)}
.arrows{display:inline-flex;gap:4px;margin-left:8px;vertical-align:middle}
.arrows i{width:9px;height:9px;border-radius:50%;background:#6f98b8}
.foot-brand{left:596px;top:16px;display:flex;align-items:center;gap:4px;color:#c5d9e8;font-family:"Tinos",serif;font-size:12.5px}
.foot-brand i{width:9px;height:9px;background:#c5d9e8}
.foot-tag{left:610px;top:32px;font-size:6px;color:#c5d9e8}
.copyright{left:606px;top:58px;font-size:8.6px;line-height:14.7px;color:var(--footer-text)}
</style>
</head>
<body>

<header class="site-header abs">
  <div class="brand abs"><span class="brand-mark"></span><span class="brand-name">Keyplot Meadow Doors</span></div>
  <p class="tagline abs">Pick the phone we will buy your home</p>
  <p class="phone abs">Call us: (555) 014-2290</p>
</header>

<nav class="main-nav abs">
  <a href="#" style="left:118px">Home</a>
  <a href="#" class="active" style="left:167px">Our Story</a>
  <a href="#" style="left:252px">Tenant</a>
  <a href="#" style="left:315px">Owner</a>
  <a href="#" style="left:376px">Contact us</a>
  <a href="#" class="account">Sign in &nbsp;/&nbsp; Sign up</a>
</nav>

<section class="hero abs"></section>

<div class="slider abs">
  <div class="slide-photo" role="img" aria-label="Photo of a two-storey craftsman house with stone steps and a wide porch under a cloudy sky">
    <div class="slide-caption">
      <h3>Multi-Unit &amp; HOA Management</h3>
      <p>We work with investors to make managing your investments easy!</p>
    </div>
  </div>
</div>
<div class="dots abs"><i></i><i></i><i class="off"></i><i></i><i></i></div>

<div class="search-tab tab-tenants abs">Tenants</div>
<div class="search-tab tab-owners abs">Oweners</div>
<form class="search-panel abs">
  <span class="lbl" style="left:22px;top:15px">Address, Suburbs, Postcodes, or Regions</span>
  <div class="field">Example: Cedar Hollow, Texas 70001</div>
  <span class="check"><svg width="11" height="11" viewBox="0 0 11 11"><path d="M2 5.5l2.5 2.5L9 3" stroke="#3b78a5" stroke-width="1.8" fill="none"/></svg></span>
  <span class="lbl" style="left:46px;top:77px">Include surrounding suburbs</span>
  <span class="lbl" style="left:26px;top:104px">Property Type :</span>
  <div class="select" style="top:100px">Select one<svg width="7" height="11" viewBox="0 0 7 11"><path d="M0 4L3.5 0 7 4zM0 7l3.5 4L7 7z" fill="#333"/></svg></div>
  <span class="lbl" style="left:43px;top:137px">Bedrooms :</span>
  <div class="select" style="top:134px">Select one<svg width="7" height="11" viewBox="0 0 7 11"><path d="M0 4L3.5 0 7 4zM0 7l3.5 4L7 7z" fill="#333"/></svg></div>
  <div class="btn-search">Search</div>
</form>

<section class="promo abs">
  <svg class="promo-red" viewBox="0 0 437 150" preserveAspectRatio="none">
    <rect width="437" height="150" fill="#eef3f8"/>
    <path d="M0 0H437V133C420 126 400 130 380 126C350 120 330 135 300 128C270 122 250 128 220 126C180 123 150 132 120 128C90 124 60 135 30 130C15 128 5 135 0 137Z" fill="#c8080c"/>
  </svg>
  <div class="badge"><b>$100</b><span>OFF</span></div>
  <div class="holiday">
    <h2>HAPPY HOLIDAYS!!!!</h2>
    <p class="sub">BE IN YOUR NEW HOME BEFORE CHRISTMAS!!</p>
    <p class="ask">ASK ABOUT OUR $100 OFF SPECIAL ON SOME<br>OF OUR HOMES MARKED *** BELOW!!</p>
  </div>
  <p class="perks">MOVE IN TODAY!!, &nbsp;LEASE TO OWN!!, &nbsp;FREE MONTHS RENT!!*<br>NO CREDIT CHECKS!!, &nbsp;NO QUALIFICATIONS!!, &nbsp;NO APPLICATION PROCESS!!<br>NO PET RESTRICTIONS!!*, &nbsp;NO SMOKER RESTRICTIONS!!*</p>
  <ul class="listings">
    <li>1027 Fernlow Dr. Garland, 75040 3/1.5/1 999 sqft. $995.00</li>
    <li>11721 Quillby Ln. Dallas, 75128 3/1/1 1092 sqft. $995.00 ?</li>
    <li>1107 Calle Serena Mesquite, 75149 3/2 1150 sqft. $1095.00***</li>
    <li>4518 Tarrow Dr. Mesquite, 75150 3/1.5/1 1018 sqft. $1195.00***</li>
    <li>1153 Ashbrook Dr. Crowley, 76036 3/2/2 1410 sqft. $1295.00***</li>
    <li>10461 Marlow Dr. Dallas, 75229 3/2/2 1392 sqft. $1295.00</li>
    <li>856 Pellam Ln. Fort Worth, 76052 3/2/2 1590 sqft. $1195.00</li>
    <li>1260 Kessing Cr. Fort Worth, 76134 3/2/2 1380 sqft. $1295.00</li>
    <li>8502 Dunmere Ave. Dallas, 75209 2/1/1 816 sqft. $1595.00***</li>
    <li>4605 Vireo Ct. Arlington, 76016 3/2/2 2450 sqft. $1495.00</li>
    <li>8601 Stillwater Bend Ln. Plano, 75024 3/2.5/2 1585 sqft. $1595.00</li>
    <li>2828 Larkspur Dr. Mesquite, 75181 3/2/2 1876 sqft. $1895.00***</li>
    <li>2782 Quiet Cove Dr. Lewisville, 75056 4/3/2 3051 sqft. $2495.00***</li>
  </ul>
</section>

<aside class="featured abs">
  <h2>Featured Listings</h2>
  <div class="card" style="top:28px">
    <div class="card-photo" role="img" aria-label="Photo of a brick two-storey house with a green lawn"></div>
    <p>4605 Vireo Court<br>Arlington, TX 76016</p>
    <svg width="24" height="22" viewBox="0 0 24 22"><circle cx="9" cy="9" r="6.5" stroke="#fff" stroke-width="2.5" fill="none"/><path d="M14 13.5l7 6" stroke="#fff" stroke-width="3.5" stroke-linecap="round"/></svg>
  </div>
  <div class="card" style="top:188px">
    <div class="card-photo" role="img" aria-label="Photo of a brick two-storey house with a green lawn"></div>
    <p>4605 Vireo Court<br>Arlington, TX 76016</p>
    <svg width="24" height="22" viewBox="0 0 24 22"><circle cx="9" cy="9" r="6.5" stroke="#fff" stroke-width="2.5" fill="none"/><path d="M14 13.5l7 6" stroke="#fff" stroke-width="3.5" stroke-linecap="round"/></svg>
  </div>
  <div class="card" style="top:348px">
    <div class="card-photo" role="img" aria-label="Photo of a brick two-storey house with a green lawn"></div>
    <p>4605 Vireo Court<br>Arlington, TX 76016</p>
    <svg width="24" height="22" viewBox="0 0 24 22"><circle cx="9" cy="9" r="6.5" stroke="#fff" stroke-width="2.5" fill="none"/><path d="M14 13.5l7 6" stroke="#fff" stroke-width="3.5" stroke-linecap="round"/></svg>
  </div>
</aside>

<section class="band abs"></section>
<form class="box abs" style="left:107px;width:314px">
  <h3>Member login</h3>
  <div class="input" style="left:16px;width:100px">User name</div>
  <div class="input" style="left:127px;width:100px">Password</div>
  <div class="btn-small" style="left:236px;width:63px">Login</div>
</form>
<form class="box abs" style="left:439px;width:313px">
  <h3>Subscribe to our weekly newsletter</h3>
  <div class="input" style="left:14px;width:207px">email address</div>
  <div class="btn-small" style="left:228px;width:72px">Subscribe</div>
</form>
<div class="signup abs"><div class="left">Not a member yet</div><div class="right">Signup Now</div></div>
<span class="social abs" style="left:439px" aria-label="Social profile"></span>
<span class="social abs" style="left:481px" aria-label="Social profile"></span>
<span class="social abs" style="left:523px" aria-label="Social profile"></span>

<footer class="site-footer abs">
  <div class="col" style="left:118px"><h4>About Us</h4><ul><li>About us</li><li>Why us</li><li>Customer Stories</li><li>Press Resources</li><li>Press Releases</li><li>Contact us</li></ul></div>
  <div class="col" style="left:244px"><h4>Proparties</h4><ul><li>Rent a home</li><li>Lease a home</li><li>Buy a home</li><li>Sell a home</li><li>Ask advices</li></ul></div>
  <div class="col" style="left:371px;width:215px"><h4>Costamer Testimonials<span class="arrows"><i></i><i></i></span></h4>
    <p>Keyplot Meadow Doors,<br>To those who do not know me, my name is Warren Hollis. I have been in the customer service/sales industry for half my life now and have been in every</p>
    <p class="sign">Warren Hollis<br>Owner, Your Steady Harbor</p>
  </div>
  <div class="foot-brand abs"><i></i>Keyplot Meadow Doors</div>
  <p class="foot-tag abs">Pick the phone we will buy your home</p>
  <p class="copyright abs">© COPYRIGHT KMD 2005<br>- ALL RIGHTS RESERVED</p>
</footer>

</body>
</html>
```